Full set of animated banner ads for Wrytelo

Wrytelo requires a full set of animated banner ads for our new blog package product:

https://uk.wrytelo.com/blog-packages

Key USPs

A blog which has regular content attracts more visitors. If a business does not have time to do this, our new product is the perfect solution. We'll supply unique, quality blog posts direct to your blog each week. Cancel or change plan any time.

Call to action

Signup to a package, enter a few details and we'll start immediately.

Specs

.GIF preferred over .SWF.
150 KB or less

Show us a couple of examples so we can pick a winner. Once we decide a winner please be ready to send files in the following sizes;

468 × 60 Banner
728 × 90 Leaderboard
250 × 250 Square
200 × 200 Small square
336 × 280 Large rectangle
300 × 250 Inline rectangle
120 × 600 Skyscraper
160 × 600 Wide skyscraper
300 × 600 Half-page ad
970 × 90 Large leaderboard
240 × 400 Vertical rectangle
980 × 120 Panorama
930 × 180 Top banner
250 × 360 Triple widescreen
580 × 400 Netboard
970 × 250 Billboard
Updates

Target Market(s)

small business owners

Industry/Entity Type

Business

```html
<!DOCTYPE html>
<html lang="en">
<head>
<meta charset="utf-8">
<title>Wrytelo – Blog Packages Banner</title>
<link rel="stylesheet" href="https://fonts.googleapis.com/css2?family=Bebas+Neue&family=Dancing+Script:wght@600&family=Montserrat:wght@300&display=swap">
<style>
  :root {
    --brand-green: #6cb444;
    --accent-green: #7cc241;
    --bar-dark: #232323;
    --gutter: #ffffff;
    --photo-dark: #3a3a3a;
    --photo-mid: #8a8a8a;
    --photo-light: #c9c9c9;
    --ink-light: #ffffff;
  }
  * { margin: 0; padding: 0; box-sizing: border-box; }
  html, body {
    width: 1200px; height: 330px; overflow: hidden;
    background: var(--gutter);
  }
  .banner-set {
    position: relative; width: 1200px; height: 330px;
  }
  .frame {
    position: absolute; top: 0; height: 330px;
    background: var(--brand-green); overflow: hidden;
  }
  .frame--intro { left: 0; width: 396px; }
  .frame--features { left: 403px; width: 393px; }
  .frame--cta { left: 803px; width: 397px; }

  .brand-bar {
    position: absolute; left: 0; right: 0; bottom: 0; height: 70px;
    background: var(--bar-dark);
    display: flex; align-items: center; padding-left: 16px; gap: 7px;
  }
  .brand-mark {
    width: 10px; height: 10px; background: var(--brand-green);
  }
  .brand-name {
    font-family: "Bebas Neue", sans-serif;
    font-size: 22px; color: var(--ink-light); letter-spacing: 0.5px;
    padding-top: 2px;
  }

  .desk-photo {
    position: absolute; left: 0; top: 0; width: 100%; height: 255px;
    background:
      radial-gradient(ellipse 120px 80px at 300px 60px, var(--photo-dark), transparent 75%),
      radial-gradient(ellipse 90px 60px at 30px 40px, var(--photo-dark), transparent 80%),
      linear-gradient(160deg, var(--photo-mid) 0%, var(--photo-light) 55%, var(--photo-mid) 100%);
  }
  .photo-rule {
    position: absolute; left: 0; right: 0; top: 255px; height: 5px;
    background: var(--brand-green);
  }
  .tagline {
    position: absolute; left: 16px; top: 118px;
    font-family: "Dancing Script", cursive;
    font-weight: 600; font-size: 40px; color: var(--ink-light);
    white-space: nowrap;
  }
  .tagline__accent { color: var(--accent-green); }

  .feature-list {
    position: absolute; left: 0; top: 36px; list-style: none;
  }
  .feature {
    display: flex; align-items: center; height: 52px;
  }
  .feature__icon {
    width: 50px; display: flex; justify-content: center; padding-left: 28px;
  }
  .feature__text {
    font-family: "Bebas Neue", sans-serif;
    font-size: 29px; color: var(--ink-light); letter-spacing: 0.3px;
    padding-left: 20px; padding-top: 3px; white-space: nowrap;
  }

  .signup-button {
    position: absolute; left: 73px; top: 110px; width: 257px; height: 63px;
    border: 2px solid var(--ink-light);
    display: flex; align-items: center; justify-content: center;
    font-family: "Montserrat", sans-serif; font-weight: 300;
    font-size: 20px; color: var(--ink-light); letter-spacing: 0.5px;
    text-decoration: none;
  }
</style>
</head>
<body>
<main class="banner-set">

  <section class="frame frame--intro">
    <div class="desk-photo" role="img" aria-label="Blurred photo of a desk with a laptop, notebook and coffee cup"></div>
    <div class="photo-rule"></div>
    <p class="tagline">Copyrighting made <span class="tagline__accent">easy</span></p>
    <footer class="brand-bar"><span class="brand-mark"></span><span class="brand-name">Wrytelo</span></footer>
  </section>

  <section class="frame frame--features">
    <ul class="feature-list">
      <li class="feature">
        <span class="feature__icon">
          <svg width="26" height="26" viewBox="0 0 26 26" aria-hidden="true">
            <path d="M3 23 L5 16 L18 3 L23 8 L10 21 Z" fill="#fff"/>
            <path d="M3 23 L5 16 L10 21 Z" fill="#6cb444" opacity="0.35"/>
          </svg>
        </span>
        <span class="feature__text">Quality copy for your blog</span>
      </li>
      <li class="feature">
        <span class="feature__icon">
          <svg width="26" height="26" viewBox="0 0 26 26" aria-hidden="true">
            <path d="M24 2 L2 11 L10 14 L13 23 Z" fill="#fff"/>
            <path d="M24 2 L10 14" stroke="#6cb444" stroke-width="1.5"/>
          </svg>
        </span>
        <span class="feature__text">Instant publishing</span>
      </li>
      <li class="feature">
        <span class="feature__icon">
          <svg width="10" height="22" viewBox="0 0 10 22" aria-hidden="true">
            <rect x="2" y="2" width="6" height="18" fill="none" stroke="#fff" stroke-width="1.5"/>
          </svg>
        </span>
        <span class="feature__text">Rapid turnaround</span>
      </li>
      <li class="feature">
        <span class="feature__icon">
          <svg width="28" height="26" viewBox="0 0 28 26" aria-hidden="true">
            <path d="M1 3 H6 L9 17 H23 L26 7 H7" fill="none" stroke="#fff" stroke-width="2.5" stroke-linejoin="round"/>
            <rect x="8" y="7" width="17" height="9" fill="#fff"/>
            <circle cx="11" cy="22" r="2.5" fill="#fff"/>
            <circle cx="21" cy="22" r="2.5" fill="#fff"/>
          </svg>
        </span>
        <span class="feature__text">No contracts</span>
      </li>
    </ul>
    <footer class="brand-bar"><span class="brand-mark"></span><span class="brand-name">Wrytelo</span></footer>
  </section>

  <section class="frame frame--cta">
    <a class="signup-button" href="https://uk.wrytelo.com/blog-packages">SIGN UP TODAY ››</a>
    <footer class="brand-bar"><span class="brand-mark"></span><span class="brand-name">Wrytelo</span></footer>
  </section>

</main>
</body>
</html>
```